Re-vamp existing website :www.harbourpathwealth.com.au

We need a new website design for this website
www.harbourpathwealth.com.au.

"creating financial lightbulb moments"

Looking for something modern, corporate like this https://www.creditvale.com.au

Imagery is important, showing really great images of what we do.

We want to keep the theme of:
Build Your Future
Invest in your Dreams
Grow You

We want a blog/opinion page on the website

Staying with our three logo colours throughout

Industry/Entity Type

Financial Service

Number of Pages Required

5+ page

```html
<!DOCTYPE html>
<html lang="en">
<head>
<meta charset="utf-8">
<title>Harbour Path Wealth Financial Group</title>
<link href="https://fonts.googleapis.com/css2?family=Raleway:wght@400;500;600;700&family=Open+Sans:wght@400;600;700&display=swap" rel="stylesheet">
<style>
:root{
  --green:#a5c63b;
  --blue:#2ba6de;
  --blue-dark:#1c8fc6;
  --ink:#2b2b2b;
  --text:#555;
  --muted:#8a8a8a;
  --light:#f4f5f6;
  --footer:#2a2a2a;
  --footer-base:#1d1d1d;
  --white:#fff;
}
*{margin:0;padding:0;box-sizing:border-box}
html,body{width:1200px;height:3158px;overflow:hidden}
body{position:relative;font-family:"Open Sans",Arial,sans-serif;color:var(--text);background:var(--white)}
.abs{position:absolute}
h1,h2,h3,h4,.nav a{font-family:"Raleway",Arial,sans-serif}

/* header */
.brand{left:162px;top:14px;display:flex;align-items:center;gap:8px}
.brand-dot{width:34px;height:34px;border-radius:50%;background:var(--blue)}
.brand-name{font-family:"Raleway",sans-serif;font-weight:700;font-size:18px;color:var(--blue);line-height:1}
.sub{font-family:"Raleway",sans-serif;font-size:11px;color:var(--muted)}
.search{left:484px;top:8px;width:180px;height:28px;border:1px solid #ddd;font-size:11px;color:#999;padding:6px 10px}
.search-btn{left:664px;top:8px;width:28px;height:28px;background:var(--green)}
.quote{left:700px;top:4px;width:172px;height:34px;background:var(--blue);color:#fff;font-size:13px;font-weight:600;padding:8px 0 0 46px;clip-path:polygon(6% 0,100% 0,100% 100%,0 100%)}
.quote-social{left:872px;top:4px;width:166px;height:34px;background:var(--green);clip-path:polygon(0 0,100% 0,90% 100%,0 100%)}
.soc{top:9px;width:22px;height:22px;border-radius:50%;background:#fff}
.contact{top:64px;display:flex;align-items:center;gap:10px;font-size:13.5px;color:#444;white-space:nowrap}
.contact .ring{width:30px;height:30px;flex:none;border-radius:50%;border:2px solid var(--blue);display:flex;align-items:center;justify-content:center}
.contact.phone{font-size:19px}
.nav{left:0;top:120px;width:1200px;height:38px;background:var(--blue)}
.nav a{position:absolute;top:0;height:38px;line-height:38px;font-size:12px;color:#fff;text-decoration:none;text-align:center;font-weight:500}
.nav a.active{background:var(--green)}

/* hero */
.hero{left:0;top:158px;width:1200px;height:452px;background:linear-gradient(180deg,#5a6f86 0%,#7d8898 35%,#4d4138 70%,#2b2420 100%)}
.hero-title{left:164px;top:268px;color:#fff;font-size:31px;line-height:37px;font-weight:700;letter-spacing:.5px}
.btn-ghost{border:2px solid #fff;color:#fff;font-size:12px;text-align:center;border-radius:4px}
.arrow{top:360px;width:26px;height:50px}

/* service bands */
.band{top:610px;height:173px}
.band-title{top:646px;color:#fff;font-size:24px;font-weight:500;letter-spacing:.5px}
.band-text{top:682px;width:290px;color:#fff;font-size:12px;line-height:20px;font-weight:600}
.center-badge{left:554px;top:632px;width:92px;height:92px;border-radius:50%;background:#fff;border:6px solid var(--blue)}

/* welcome */
.welcome-title{left:162px;top:828px;font-size:26px;font-weight:500;color:var(--ink);letter-spacing:.5px}
.welcome-title span{color:var(--green)}
.divider-dot{width:14px;height:14px;border-radius:50%;border:2px solid #cfcfcf}
.lead{font-size:14px;line-height:22px;color:#333}
.body{font-size:12.5px;line-height:21px;color:#555}
.btn-outline{border:2px solid var(--blue);color:var(--blue);font-size:12px;text-align:center;border-radius:4px}
.portrait{left:825px;top:836px;width:212px;height:243px;background:var(--blue);padding:8px}
.portrait .photo{width:196px;height:175px;background:linear-gradient(180deg,#e8edf1,#9aa7b3)}
.portrait .name{color:#fff;text-align:center;font-weight:700;font-size:17px;margin-top:10px}
.portrait .role{color:#fff;text-align:center;font-size:11px}

/* services */
.services{left:0;top:1137px;width:1200px;height:484px;background:linear-gradient(135deg,#2ba6de,#35b0e6 50%,#1f9ad4)}
.services-title{left:0;width:1200px;text-align:center;top:42px;color:#fff;font-size:24px;font-weight:500;letter-spacing:.5px}
.services-intro{left:0;width:1200px;text-align:center;top:104px;color:#fff;font-size:12.5px}

/* journey */
.journey-title{left:0;width:1200px;text-align:center;top:1674px;font-size:24px;font-weight:600;color:var(--ink)}
.journey-title span{color:var(--green)}
.para{left:170px;width:860px;text-align:center;font-size:11.5px;line-height:19px;color:#444}
.step-label{width:180px;text-align:center;font-size:13px;line-height:18px;color:#333}
.btn-cta{left:468px;top:2188px;width:292px;height:40px;border:2px solid var(--blue);color:var(--blue);font-size:13px;line-height:36px;text-align:center}

/* blog & testimonials */
.feature{left:0;top:2284px;width:1200px;height:358px;background:var(--light)}
.sec-title{font-size:26px;font-weight:500;color:var(--ink)}
.sec-title span{color:var(--green)}
.view-all{width:90px;height:34px;border:2px solid var(--blue);color:var(--blue);font-size:12px;line-height:30px;text-align:center;border-radius:3px;background:#fff}
.date{width:42px;height:52px;text-align:center;color:#fff}
.date .d{background:var(--blue);height:30px;font-size:18px;font-weight:700;line-height:30px}
.date .m{background:var(--green);height:22px;font-size:12px;line-height:22px}
.post h4{font-size:15.5px;font-weight:700;color:#222}
.post p{font-size:11.5px;line-height:17px;color:#555}
.quote-box{left:652px;top:2400px;width:388px;height:104px;background:#fff;border:1px solid #e1e1e1;border-radius:8px;padding:14px 22px 0 40px;font-style:italic;font-size:11.5px;line-height:18px;color:#444}
.client-name{left:724px;top:2514px;font-weight:700;font-size:13px;color:#222}
.client-role{left:838px;top:2514px;font-size:13px;color:#444}

/* partners */
.partners{left:0;top:2642px;width:1200px;height:151px;background:#fafafa}
.partner{top:2684px;width:130px;height:64px;background:#fff;border:1px solid #e3e3e3}
.partner i{position:absolute;left:30px;top:24px;width:70px;height:16px;border-radius:8px}

/* footer */
.footer{left:0;top:2793px;width:1200px;height:322px;background:var(--footer)}
.footer-title{top:2834px;color:#fff;font-size:14px;font-weight:700}
.footer-links{left:166px;top:2864px;list-style:none;color:#ddd;font-size:11.5px;line-height:19px}
.footer-links li::before{content:"›";margin-right:8px;color:#bbb}
.footer-info{color:#ddd;font-size:11.5px;line-height:17px}
.note{left:0;width:1200px;text-align:center;color:#ccc;font-size:11.5px;line-height:22px;top:3046px}
.base{left:0;top:3115px;width:1200px;height:43px;background:var(--footer-base);color:#ddd;font-size:11.5px}
.base-soc{top:10px;width:22px;height:22px;border-radius:50%;background:#fff}
</style>
</head>
<body>

<!-- header -->
<div class="abs brand">
  <div class="brand-dot"></div>
  <div>
    <div class="brand-name">harbourpathwealth</div>
    <div class="sub" style="font-size:10px;letter-spacing:2px;color:var(--blue)">FINANCIAL GROUP</div>
  </div>
</div>
<div class="abs search">Search</div>
<div class="abs search-btn"><svg width="28" height="28" viewBox="0 0 28 28"><circle cx="13" cy="13" r="5" fill="none" stroke="#fff" stroke-width="2"/><line x1="17" y1="17" x2="21" y2="21" stroke="#fff" stroke-width="2"/></svg></div>
<div class="abs quote">
  <svg class="abs" style="left:20px;top:9px" width="18" height="16" viewBox="0 0 18 16"><rect x="1" y="3" width="12" height="12" fill="none" stroke="#fff" stroke-width="1.6"/><path d="M7 10 L16 1" stroke="#fff" stroke-width="1.8"/></svg>
  GET FREE QUOTE
</div>
<div class="abs quote-social"></div>
<div class="abs soc" style="left:890px"></div>
<div class="abs soc" style="left:920px"></div>
<div class="abs soc" style="left:950px"></div>
<div class="abs soc" style="left:980px"></div>
<div class="abs contact" style="left:556px">
  <span class="ring"><svg width="14" height="10" viewBox="0 0 14 10"><rect x=".5" y=".5" width="13" height="9" fill="none" stroke="#2ba6de"/><path d="M.5 .5 L7 6 L13.5 .5" fill="none" stroke="#2ba6de"/></svg></span>
  theteam@harbourpathwealth.com.au
</div>
<div class="abs contact phone" style="left:880px">
  <span class="ring"><svg width="14" height="14" viewBox="0 0 14 14"><path d="M3 1 L5 4 L4 6 Q6 9 8 10 L10 9 L13 11 L11 13 Q5 13 1 3 Z" fill="#2ba6de"/></svg></span>
  0400 555 019
</div>

<nav class="abs nav">
  <a class="active" href="#" style="left:162px;width:116px">HOME</a>
  <a href="#" style="left:290px;width:120px">ABOUT US</a>
  <a href="#" style="left:440px;width:120px">HOME LOANS</a>
  <a href="#" style="left:600px;width:150px">BUSINESS LENDING</a>
  <a href="#" style="left:770px;width:110px">BLOG</a>
  <a href="#" style="left:900px;width:140px">CONTACT US</a>
</nav>

<!-- hero -->
<div class="abs hero" role="img" aria-label="Photo of a hand passing house keys to an open hand in front of a new home"></div>
<h1 class="abs hero-title">CREATING FINANCIAL<br>LIGHTBULB MOMENTS</h1>
<div class="abs btn-ghost" style="left:162px;top:358px;width:118px;height:38px;line-height:34px">Read More</div>
<svg class="abs arrow" style="left:74px" viewBox="0 0 26 50"><path d="M22 2 L4 25 L22 48" fill="none" stroke="#fff" stroke-width="2"/></svg>
<svg class="abs arrow" style="left:1100px" viewBox="0 0 26 50"><path d="M4 2 L22 25 L4 48" fill="none" stroke="#fff" stroke-width="2"/></svg>

<!-- service bands -->
<div class="abs band" style="left:0;width:600px;background:var(--green)"></div>
<div class="abs band" style="left:600px;width:600px;background:var(--blue)"></div>
<svg class="abs" style="left:158px;top:670px" width="70" height="56" viewBox="0 0 70 56"><path d="M35 2 L68 30 L60 30 L60 54 L42 54 L42 38 L28 38 L28 54 L10 54 L10 30 L2 30 Z" fill="#fff"/></svg>
<h2 class="abs band-title" style="left:258px">HOME LOANS</h2>
<p class="abs band-text" style="left:258px">Lorem Ipsum is simply dummy text of the printing and typesetting industry. Lorem Ipsum has been the industry's strd... [Learn More]</p>
<div class="abs center-badge"></div>
<h2 class="abs band-title" style="left:706px">BUSINESS LENDING</h2>
<p class="abs band-text" style="left:666px">Lorem Ipsum is simply dummy text of the printing and typesetting industry. Lorem Ipsum has been the industry's strd... [Learn More]</p>
<svg class="abs" style="left:982px;top:656px" width="58" height="74" viewBox="0 0 58 74"><rect x="4" y="10" width="24" height="62" fill="none" stroke="#fff" stroke-width="3"/><rect x="28" y="26" width="24" height="46" fill="none" stroke="#fff" stroke-width="3"/><g fill="#fff"><rect x="10" y="18" width="4" height="5"/><rect x="18" y="18" width="4" height="5"/><rect x="10" y="30" width="4" height="5"/><rect x="18" y="30" width="4" height="5"/><rect x="10" y="42" width="4" height="5"/><rect x="18" y="42" width="4" height="5"/><rect x="34" y="34" width="4" height="5"/><rect x="42" y="34" width="4" height="5"/><rect x="34" y="46" width="4" height="5"/><rect x="42" y="46" width="4" height="5"/></g></svg>

<!-- welcome -->
<section class="welcome">
  <h2 class="abs welcome-title">WELCOME TO <span>HARBOUR PATH WEALTH</span></h2>
  <div class="abs sub" style="left:464px;top:862px">FINANCIAL GROUP</div>
  <div class="abs divider-dot" style="left:162px;top:880px"></div>
  <p class="abs lead" style="left:162px;top:914px;width:610px">We are a leading Australian finance brokerage group dedicated to providing our clients with a range of financial solutions tailored to their requirements.</p>
  <p class="abs body" style="left:162px;top:966px;width:610px">Our goal is to become your trusted partner throughout the entire lending process and beyond. We will implement the loan process from application to settlement, handle all negotiations and drive all communication and paperwork with the relevant parties to ensure your peace of mind.</p>
  <div class="abs btn-outline" style="left:162px;top:1044px;width:116px;height:38px;line-height:34px">Read More</div>
  <div class="abs portrait">
    <div class="photo" role="img" aria-label="Portrait photo of the director in a suit"></div>
    <div class="name">Marcus Ellery</div>
    <div class="role">Director</div>
  </div>
</section>

<!-- services -->
<section class="abs services" role="img" aria-label="Our services diagram">
  <h2 class="abs services-title">OUR SERVICES</h2>
  <div class="abs divider-dot" style="left:593px;top:80px;border-color:#bfe3f5"></div>
  <div class="abs services-intro">Our accredited and experienced team specialise in:</div>
  <svg class="abs" style="left:0;top:0" width="1200" height="484" viewBox="0 0 1200 484">
    <g stroke="#fff" stroke-width="2" fill="none">
      <path d="M596 338 L596 268"/>
      <path d="M520 360 L474 300"/>
      <path d="M672 360 L716 300"/>
      <path d="M470 400 L430 372 L396 372"/>
      <path d="M722 400 L760 372 L785 372"/>
      <path d="M456 440 L392 436"/>
      <path d="M736 440 L786 436"/>
    </g>
    <g fill="#fff">
      <circle cx="596" cy="338" r="5"/><circle cx="520" cy="360" r="5"/><circle cx="672" cy="360" r="5"/>
      <circle cx="470" cy="400" r="5"/><circle cx="722" cy="400" r="5"/><circle cx="456" cy="440" r="5"/><circle cx="736" cy="440" r="5"/>
    </g>
    <g fill="#fff" stroke="#2ba6de" stroke-width="3">
      <circle cx="596" cy="235" r="32"/>
      <circle cx="474" cy="269" r="32"/>
      <circle cx="716" cy="269" r="32"/>
      <circle cx="396" cy="341" r="32"/>
      <circle cx="785" cy="341" r="32"/>
      <circle cx="821" cy="432" r="32"/>
    </g>
    <circle cx="358" cy="432" r="32" fill="#a5c63b" stroke="#fff" stroke-width="3"/>
    <g fill="none" stroke="#2ba6de" stroke-width="2.4">
      <rect x="462" y="257" width="24" height="24"/><path d="M468 275 V267 M474 275 V262 M480 275 V270"/>
      <circle cx="714" cy="267" r="9"/><path d="M721 274 L728 281"/>
      <circle cx="785" cy="341" r="14"/><path d="M785 332 V350 M780 336 H789 M781 346 H790"/>
      <path d="M585 246 L596 226 L607 246 Z"/><path d="M596 246 V236"/>
      <path d="M386 348 L396 332 L406 348 M396 348 V338"/>
      <path d="M809 444 V428 L815 422 L821 428 V444 M823 444 V424 L829 418 L835 424 V444"/>
    </g>
    <path d="M346 442 V430 L358 420 L370 430 V442 Z" fill="#fff"/>
    <path d="M446 484 A150 150 0 0 1 746 484 Z" fill="#fff" stroke="#1c8fc6" stroke-width="6"/>
    <circle cx="556" cy="440" r="9" fill="#2ba6de"/>
    <text x="572" y="445" font-family="Raleway, sans-serif" font-weight="700" font-size="15" fill="#2ba6de">harbourpath</text>
    <text x="596" y="466" text-anchor="middle" font-family="Raleway, sans-serif" font-size="9" letter-spacing="2" fill="#2ba6de">FINANCIAL GROUP</text>
    <g font-family="Raleway, sans-serif" font-weight="700" font-size="17" fill="#fff">
      <text x="596" y="180" text-anchor="middle">BUSINESS LOAN</text>
      <text x="232" y="273">COMMERCIAL LOAN</text>
      <text x="777" y="273">DEVELOPMENT LOAN</text>
      <text x="162" y="347">INVESTMENT LOAN</text>
      <text x="844" y="347">INCOME PROTECTION</text>
      <text x="187" y="438">HOME LOAN</text>
      <text x="880" y="438">PROPETY INVESTING</text>
    </g>
  </svg>
</section>

<!-- journey -->
<section class="journey">
  <h2 class="abs journey-title">HOW YOUR HPW <span>JOURNEY WORKS</span></h2>
  <div class="abs divider-dot" style="left:593px;top:1718px"></div>
  <p class="abs para" style="top:1752px">Harbour Path Wealth (HPW) is a leading Australian finance brokerage group dedicated in providing our clients with a range of financial solutions tailored to their individual requirements. We want our clients to be bold in chasing their financial dreams and we commit to provide a range of opportunities for them to do so.</p>
  <p class="abs para" style="top:1806px">Harbour Path Wealth aims to push the status quo by doing things differently. We want you to start thinking BIG and we can show you the steps to get you there. We know you have your vision of where you want to be, we will provide the guidance you might need in getting there.</p>
  <svg class="abs" style="left:0;top:1890px" width="1200" height="210" viewBox="0 0 1200 210">
    <g stroke-width="22" fill="#fff">
      <circle cx="257" cy="80" r="68" stroke="#a5c63b"/>
      <circle cx="490" cy="80" r="68" stroke="#2ba6de"/>
      <circle cx="728" cy="80" r="68" stroke="#a5c63b"/>
      <circle cx="962" cy="80" r="68" stroke="#a5c63b"/>
    </g>
    <g fill="none" stroke-width="5">
      <rect x="230" y="56" width="46" height="46" rx="4" stroke="#a5c63b"/>
      <path d="M248 88 L280 56" stroke="#a5c63b"/>
      <rect x="466" y="58" width="48" height="44" stroke="#2ba6de"/>
      <path d="M478 94 V80 M490 94 V70 M502 94 V76" stroke="#2ba6de"/>
      <path d="M714 72 V62 A14 14 0 0 1 742 62 V72" stroke="#a5c63b"/>
      <rect x="940" y="56" width="44" height="44" stroke="#a5c63b"/>
      <path d="M948 76 L960 90 L986 58" stroke="#a5c63b"/>
    </g>
    <rect x="706" y="72" width="44" height="34" rx="3" fill="#a5c63b"/>
    <circle cx="728" cy="86" r="5" fill="#fff"/>
  </svg>
  <div class="abs step-label" style="left:167px;top:2110px">1. Our HPW Mapping Session - Identifying your BIG Ideas &amp; Goals</div>
  <div class="abs step-label" style="left:400px;top:2110px;color:var(--blue)">2. Structure &amp; Strategy</div>
  <div class="abs step-label" style="left:638px;top:2110px">3. Protect</div>
  <div class="abs step-label" style="left:872px;top:2110px">4. Implementation &amp;<br>Review</div>
  <div class="abs btn-cta">CLICK HERE TO START YOUR JOURNEY!</div>
</section>

<!-- blog & testimonials -->
<div class="abs feature"></div>
<h3 class="abs sec-title" style="left:162px;top:2334px">LATEST <span>BLOG</span></h3>
<div class="abs view-all" style="left:470px;top:2336px">View All</div>
<div class="abs divider-dot" style="left:162px;top:2374px"></div>
<div class="abs" style="left:600px;top:2330px;width:1px;height:260px;background:#ddd"></div>
<div class="abs post" style="left:162px;top:2408px;width:400px">
  <div class="abs date" style="left:0;top:0"><div class="d">30</div><div class="m">Mar</div></div>
  <h4 class="abs" style="left:54px;top:-2px;width:350px">Lorem Ipsum Dolor Sit Amet</h4>
  <p class="abs" style="left:54px;top:22px;width:350px">Lorem ipsum dolor sit amet, sed diam nonummy nibh eiod tincidunt ut laoreet dolore. Sit amet, sed diam nonu +</p>
</div>
<div class="abs" style="left:162px;top:2480px;width:400px;height:1px;background:#ccc"></div>
<div class="abs post" style="left:162px;top:2500px;width:400px">
  <div class="abs date" style="left:0;top:0"><div class="d">30</div><div class="m">Mar</div></div>
  <h4 class="abs" style="left:54px;top:-2px;width:350px">Lorem Ipsum Dolor Sit Amet</h4>
  <p class="abs" style="left:54px;top:22px;width:350px">Lorem ipsum dolor sit amet, sed diam nonummy nibh emod tincidunt ut laoreet dolore. Sit amet, sed diam nonu +</p>
</div>
<div class="abs" style="left:162px;top:2572px;width:400px;height:1px;background:#ccc"></div>

<h3 class="abs sec-title" style="left:636px;top:2334px">CLIENT <span>TESTIMONIALS</span></h3>
<div class="abs view-all" style="left:950px;top:2336px">View All</div>
<div class="abs divider-dot" style="left:636px;top:2374px"></div>
<div class="abs quote-box">
  <svg class="abs" style="left:12px;top:14px" width="20" height="16" viewBox="0 0 20 16"><path d="M0 16 V8 Q0 0 8 0 V4 Q4 4 4 8 H8 V16 Z M11 16 V8 Q11 0 19 0 V4 Q15 4 15 8 H19 V16 Z" fill="#ccc"/></svg>
  Lorem ipsum dolor sit amet, sed diam nonummy nibh euismod tincidunt ut laoreet dolore. Lorem ipsum dolor sit amet, sed diam nonummy nibh euismod tincidunt ut laoreet dolore. Lorem ipsum dolor sit amet, sed diam nonummyod
</div>
<div class="abs" role="img" aria-label="Client photo" style="left:638px;top:2500px;width:70px;height:70px;border-radius:50%;background:linear-gradient(160deg,#d9c4b0,#8c6b52);border:3px solid #fff"></div>
<div class="abs" style="left:694px;top:2548px;width:30px;height:30px;border-radius:50%;background:var(--green)"></div>
<div class="abs client-name">Tessa Brooke</div>
<div class="abs" style="left:826px;top:2514px;width:1px;height:18px;background:#ccc"></div>
<div class="abs client-role">Customer</div>

<!-- partners -->
<div class="abs partners"></div>
<svg class="abs" style="left:100px;top:2690px" width="30" height="54" viewBox="0 0 30 54"><path d="M26 2 L4 27 L26 52" fill="none" stroke="#bbb" stroke-width="2"/></svg>
<svg class="abs" style="left:1064px;top:2690px" width="30" height="54" viewBox="0 0 30 54"><path d="M4 2 L26 27 L4 52" fill="none" stroke="#bbb" stroke-width="2"/></svg>
<div class="abs partner" style="left:162px"><i style="background:#c8d7e8"></i></div>
<div class="abs partner" style="left:310px"><i style="background:#cfe0ef"></i></div>
<div class="abs partner" style="left:458px"><i style="background:#dce8c4"></i></div>
<div class="abs partner" style="left:606px"><i style="background:#d8d8d8"></i></div>
<div class="abs partner" style="left:754px"><i style="background:#c6dcef"></i></div>
<div class="abs partner" style="left:902px"><i style="background:#f0dcc0"></i></div>

<!-- footer -->
<footer class="abs footer"></footer>
<h4 class="abs footer-title" style="left:162px">Quick Links</h4>
<ul class="abs footer-links">
  <li>Home</li><li>About Us</li><li>Home Loans</li><li>Business Lending</li><li>Blog</li><li>Contact Us</li>
</ul>
<h4 class="abs footer-title" style="left:328px">Contact Information</h4>
<div class="abs footer-info" style="left:328px;top:2864px">
  <span style="color:var(--blue)">HARBOUR PATH WEALTH</span><br>Suite 4, Level 3 21 Quay Lane<br>Harbourview NSW 2099
</div>
<div class="abs footer-info" style="left:328px;top:2928px">☎&nbsp;&nbsp; 0400 555 019</div>
<div class="abs footer-info" style="left:328px;top:2960px">✉&nbsp;&nbsp; theteam@harbourpathwealth.com.au</div>
<h4 class="abs footer-title" style="left:584px">Location Map</h4>
<div class="abs" role="img" aria-label="Street map showing the office location" style="left:584px;top:2862px;width:210px;height:124px;background:linear-gradient(135deg,#e9ecef,#cfd8e2 60%,#dde6c9)"></div>
<div class="abs" style="left:922px;top:2844px;display:flex;align-items:center;gap:6px">
  <div style="width:18px;height:18px;border-radius:50%;background:#777"></div>
  <div style="font-family:'Raleway',sans-serif;font-weight:700;font-size:14px;color:#888">harbourpath</div>
</div>
<div class="abs" style="left:940px;top:2920px;width:70px;height:70px;border-radius:50%;background:#d8b23a"></div>
<p class="abs note">At Harbour Path Wealth our team is on the road everyday and we're able to come to you at your preferred location.<br>Note: our mobile service is for the Sydney Area only.</p>
<div class="abs base">
  <div class="abs" style="left:162px;top:13px">© 2017 <span style="color:var(--blue)">HARBOUR PATH WEALTH</span> | All Rights Reserved</div>
  <div class="abs base-soc" style="left:926px"></div>
  <div class="abs base-soc" style="left:956px"></div>
  <div class="abs base-soc" style="left:986px"></div>
  <div class="abs base-soc" style="left:1016px"></div>
</div>

</body>
</html>
```